Quorvane Solutions Open House Invitation: Help us impress!

We will be having an open house, cyber security seminars, free food, free beer and wine. We will have business partners with tables to discuss potential client needs. Has to be a 2-sided invitation. I don't know the standard size, but no bigger than a 1/2 sheet of paper. Will be professionally printed when done.

We want existing and potential clients to show up and mingle, learn a little bit, and enjoy themselves!

Target Market(s)

Existing and potential clients, 90% Medical. Looking for something clean, modern and classy.

Industry/Entity Type

It Company

Colors

Designer to choose colors to be used in the design.

Requirements
Must have
• FRONT:
• [Quorvane Solutions Logo]
• "Invites you to visit our new facility and meet our team at our 'Open House'"
• Date: Friday February 28th 4-7pm
• Music, free food trucks, free beer and wine
• 27461 Marbrook place suite 308 Tampa Fl 33619
• 813-555-0172
• RSVP @ www.quorvanesolutions.example/RSVP
• BACK:
• "Meet with the People we partner with"
• Premier Sponsor
• [ZK logo]
• sponsors
• [Brindle Associates logo]
• [Pinemarsh Underwriters (PMU) Logo]
• [Systems Kept Steady logo]
• [Harrow Bank logo]
• [Lodestar Commerce logo]
• [keelwise logo]
• We will be giving away:
• 2 - ZK Lpatops ($850 Value each)
• 4 - $100 Casa Do Fogareu Giftcards
• And More!
• Cyber-Security Seminars
• 4:15 pm
• 5:15 pm
• 6:15 pm
• RSVP and additional details @ www.quorvanesolutions.example/RSVP
Nice to have
• Even though the Quorvane logo is Blue, we really like teal. Feel free to change the color. We are looking for Grey background.

```html
<!DOCTYPE html>
<html lang="en">
<head>
<meta charset="utf-8">
<title>Quorvane Solutions Open House Invitation</title>
<link href="https://fonts.googleapis.com/css2?family=Montserrat:wght@500;600;700;800&family=Open+Sans:wght@400;600&display=swap" rel="stylesheet">
<style>
  :root {
    --teal: #148a84;
    --navy: #1d3b70;
    --grey: #8f8f8f;
    --grey-light: #c9c9c9;
    --ink: #1a1a1a;
    --white: #ffffff;
    --rule: #b47f86;
  }
  * { box-sizing: border-box; margin: 0; padding: 0; }
  html, body { width: 1200px; height: 1200px; overflow: hidden; background: var(--white); }
  body { position: relative; font-family: "Open Sans", Arial, sans-serif; color: var(--ink); }

  .sheet-frame {
    position: absolute; left: 37px; top: 37px; width: 1126px; height: 1126px;
    border: 1px solid var(--grey-light);
  }

  /* ---------- Back side ---------- */
  .card-back {
    position: absolute; left: 37px; top: 212px; width: 540px; height: 771px;
    background: var(--teal); color: var(--white);
    font-family: "Montserrat", Arial, sans-serif;
  }
  .card-back .inner-rule {
    position: absolute; left: 31px; top: 31px; right: 31px; bottom: 31px;
    border: 1px solid var(--rule);
  }
  .card-back .abs { position: absolute; }
  .card-back .centered { left: 0; right: 0; text-align: center; }
  .back-title { top: 88px; font-size: 23px; font-weight: 500; }
  .section-label { left: 71px; font-size: 17px; font-weight: 500; }
  .premier-label { top: 142px; }
  .sponsors-label { top: 236px; }

  .partner {
    position: absolute; display: flex; align-items: center; justify-content: center; gap: 7px;
    font-family: "Montserrat", Arial, sans-serif; font-weight: 700; color: var(--white);
    white-space: nowrap;
  }
  .partner .mark { width: 10px; height: 10px; background: var(--white); flex: none; }
  .partner .mark.round { border-radius: 50%; width: 26px; height: 26px; }
  .partner-premier { left: 170px; top: 175px; width: 200px; height: 44px; font-size: 22px; }
  .partner-brindle { left: 80px; top: 282px; width: 210px; height: 40px; font-size: 16px; }
  .partner-steady { left: 300px; top: 282px; width: 160px; height: 40px; font-size: 12px; }
  .partner-pinemarsh { left: 120px; top: 336px; width: 280px; height: 34px; font-size: 16px; }
  .partner-harrow { left: 92px; top: 385px; width: 110px; height: 36px; font-size: 12px; }
  .partner-lodestar { left: 200px; top: 385px; width: 120px; height: 36px; font-size: 12px; }
  .partner-keelwise { left: 322px; top: 385px; width: 104px; height: 36px; font-size: 12px; }

  .giveaway-title { top: 470px; font-size: 21px; font-weight: 500; }
  .giveaway-list { top: 514px; font-family: "Open Sans", Arial, sans-serif; font-size: 13.5px; line-height: 19.5px; list-style: none; }
  .seminar-title { top: 590px; font-size: 19px; font-weight: 500; }
  .seminar-list {
    top: 622px; font-family: "Open Sans", Arial, sans-serif; font-size: 13px; line-height: 19px;
    list-style: none;
  }
  .seminar-list li::before { content: "\2022"; margin-right: 6px; }

  /* ---------- Front side ---------- */
  .card-front {
    position: absolute; left: 617px; top: 212px; width: 541px; height: 759px;
    background: var(--white); border: 1.5px solid var(--ink); overflow: hidden;
  }
  .card-front .wave { position: absolute; left: 0; top: 0; width: 541px; height: 759px; }
  .card-front .abs { position: absolute; }

  .brand-name {
    left: 42px; top: 78px;
    font-family: "Montserrat", Arial, sans-serif; font-weight: 600;
    font-size: 26px; line-height: 1; color: var(--teal); white-space: nowrap;
  }

  .invite-line { left: 0; width: 320px; top: 212px; text-align: center; font-size: 13px; line-height: 17px; color: var(--grey); }
  .open-house { left: 0; width: 320px; top: 266px; text-align: center; font-family: "Montserrat", Arial, sans-serif; font-weight: 800; font-size: 29px; color: var(--navy); }

  .info-head { left: 48px; font-family: "Montserrat", Arial, sans-serif; font-weight: 500; color: var(--teal); font-size: 17px; }
  .info-body { left: 48px; font-size: 13px; line-height: 17px; color: var(--ink); }
  .join-head { top: 358px; }
  .join-body { top: 386px; }
  .when-head { top: 430px; }
  .when-body { top: 456px; }
  .when-body .addr { padding-left: 14px; display: block; }
  .rsvp-head { top: 512px; font-size: 20px; }
  .rsvp-body { top: 541px; font-weight: 600; }

  .phone-rule { left: 35px; top: 702px; width: 106px; height: 22px; }
  .phone-number { left: 48px; top: 728px; font-size: 13px; color: var(--ink); }
</style>
</head>
<body>
  <div class="sheet-frame"></div>

  <!-- Back side -->
  <section class="card-back">
    <div class="inner-rule"></div>
    <h2 class="abs centered back-title">Meet with the People we partner with</h2>

    <p class="abs section-label premier-label">Premier Sponsor</p>
    <div class="partner partner-premier"><span class="mark round"></span>ZK</div>

    <p class="abs section-label sponsors-label">Sponsors</p>
    <div class="partner partner-brindle"><span class="mark"></span>Brindle Associates</div>
    <div class="partner partner-steady"><span class="mark"></span>Systems Kept Steady</div>
    <div class="partner partner-pinemarsh"><span class="mark"></span>PMU Pinemarsh Underwriters</div>
    <div class="partner partner-harrow">Harrow Bank</div>
    <div class="partner partner-lodestar">Lodestar Commerce</div>
    <div class="partner partner-keelwise"><span class="mark"></span>keelwise</div>

    <h3 class="abs centered giveaway-title">We will be giving away:</h3>
    <ul class="abs centered giveaway-list">
      <li>2 - ZK Lpatops ($850 Value each)</li>
      <li>4 - $100 Casa Do Fogareu Giftcards</li>
      <li>And More!</li>
    </ul>

    <h3 class="abs centered seminar-title">Cyber-Security Seminars</h3>
    <ul class="abs centered seminar-list">
      <li>4:15 pm</li>
      <li>5:15 pm</li>
      <li>6:15 pm</li>
    </ul>
  </section>

  <!-- Front side -->
  <section class="card-front">
    <svg class="wave" viewBox="0 0 541 759" aria-hidden="true">
      <path fill="#9c9c9c" d="M284,0 C364,40 484,100 454,190 C424,280 344,330 384,420 C424,510 544,560 484,660 C454,710 404,740 384,759 L541,759 L541,0 Z"/>
      <path fill="#148a84" d="M300,0 C380,40 500,100 470,190 C440,280 360,330 400,420 C440,510 560,560 500,660 C470,710 420,740 400,759 L541,759 L541,0 Z"/>
    </svg>

    <p class="abs brand-name">Quorvane Solutions</p>

    <p class="abs invite-line">Invites you to visit our new facility &amp;<br>meet our team at our</p>
    <h1 class="abs open-house">OPEN HOUSE</h1>

    <h3 class="abs info-head join-head">JOIN US FOR</h3>
    <p class="abs info-body join-body">Music, free food trucks, free beer and wine</p>

    <h3 class="abs info-head when-head">SEE YOU THERE</h3>
    <p class="abs info-body when-body">Friday February 28th | 4-7pm<br>27461 Marbrook place suite 308<span class="addr">Tampa Fl 33619</span></p>

    <h3 class="abs info-head rsvp-head">RSVP</h3>
    <p class="abs info-body rsvp-body">www.quorvanesolutions.example/RSVP</p>

    <svg class="abs phone-rule" viewBox="0 0 106 22" aria-hidden="true">
      <line x1="0" y1="11" x2="42" y2="11" stroke="#148a84" stroke-width="1"/>
      <line x1="64" y1="11" x2="106" y2="11" stroke="#148a84" stroke-width="1"/>
      <circle cx="53" cy="11" r="8" fill="none" stroke="#148a84" stroke-width="1.2"/>
      <path d="M49.5,7.5 l2,-0.5 l1,2.5 l-1.2,0.9 a6,6 0 0 0 2.8,2.8 l0.9,-1.2 l2.5,1 l-0.5,2 a8,8 0 0 1 -7.5,-7.5 z" fill="#148a84"/>
    </svg>
    <p class="abs phone-number">813-555-0172</p>
  </section>
</body>
</html>
```